Web design for Frostwerkly.com

We need a website (4 starter pages) designed for a drupal based site. The theme is flexible so I am open to different designs/looks. I am looking for a VERY simple and clean and FUN design to make it easy to use for the customer.

Our company is similar to Pitch lantern as in it's for multiple people to design a cake for a customer and they choose a winning design and work with that cake designer to make the cake (birthday, wedding etc...)

Our vision:
First page:
2 main images for either the customer to submit an idea for a cake, or the new designer to sign up to the site. Perhaps a mouse-over with wording on what the options are? You can use this site:
http://www.plumwidget.example/ as a sort of template but more clean and simple

"How it works" page:
Similar to this:
http://www.plumwidget.example/how-it-works
Fun, clean and simple

Submit cake design page (form submission)

Submit new designer page

Ideally a 960 wide design with no flash, but open to a flash design if it stands out...

Please contact me if you have any questions!

Target Market(s)

People who want a custom cake made, and people who design and make cakes.

Industry/Entity Type

Wedding

Requirements
Must have
• Use the logo attached. The "Tater Bop" should be a big part of the site...kind of a site mascot?
Nice to have
• 960 wide
No flash but not a deal-breaker if there is flash and it's amazing...

```html
<!DOCTYPE html>
<html lang="en">
<head>
<meta charset="utf-8">
<title>Frostwerkly.com</title>
<link href="https://fonts.googleapis.com/css2?family=Fredoka:wght@500;600&family=Noto+Sans:ital,wght@0,400;0,700;1,400&display=swap" rel="stylesheet">
<style>
:root{
  --brown-dark:#5c4034;
  --brown-text:#4a3a33;
  --brown-title:#8b6a5c;
  --page:#efe8e2;
  --panel:#ddd3ce;
  --nav-pink:#e4a8b7;
  --nav-line:#c98797;
  --pink:#d7387a;
  --green:#8cb544;
  --orange:#e07b26;
  --date:#c2431c;
  --footer-text:#efe4dc;
  --star-gold:#f1c21b;
  --star-grey:#c9c5c2;
  --cherry:#b9302f;
}
*{box-sizing:border-box;margin:0;padding:0}
html,body{width:1030px;height:1200px;overflow:hidden}
body{position:relative;background:var(--page);font-family:"Noto Sans",sans-serif;color:var(--brown-text)}
.abs{position:absolute}
.topbar{left:0;top:0;width:1030px;height:42px;background:var(--brown-dark)}
.topbar .phone{right:46px;top:11px;font-size:14px;color:#f6dde3}
.logo{left:52px;top:84px;display:flex;align-items:center;gap:8px;font-size:28px;font-weight:700;color:var(--brown-dark)}
.logo .dot{width:26px;height:26px;border-radius:50%;background:var(--nav-pink)}
.cta{font-family:"Fredoka",sans-serif;font-weight:600;color:#fff;font-size:16px;line-height:21px;text-shadow:0 1px 2px rgba(0,0,0,.25)}
.ph{display:block}
.nav-frame{left:44px;top:161px;width:942px;height:304px;background:var(--nav-pink);border-radius:4px;box-shadow:0 2px 4px rgba(0,0,0,.2)}
.nav{left:44px;top:161px;height:46px;display:flex;font-size:14px;color:var(--brown-text)}
.nav a{display:flex;align-items:center;justify-content:center;height:46px;border-right:1px solid var(--nav-line);text-decoration:none;color:inherit}
.nav a:last-child{border-right:0}
.nav a.active{color:#222}
.hero{left:51px;top:207px;width:928px;height:251px;background:linear-gradient(90deg,#f2ece6 0%,#f7f3ef 45%,#ece6e2 100%)}
.hero-cake{left:51px;top:207px;width:330px;height:251px;background:linear-gradient(180deg,#d85a6e 0%,#f1e6cf 45%,#c23a55 100%);opacity:.85}
.hero-title{left:384px;top:241px;font-size:28px;font-weight:700;color:var(--brown-title)}
.rating{left:385px;top:291px;display:flex;align-items:center;gap:6px;font-size:12px;color:#8b2d4a}
.hero-more{left:477px;top:325px;font-size:13px;color:#5c4a42;text-decoration:underline}
.dots{left:831px;top:428px;width:148px;height:30px;background:var(--nav-pink);border-radius:8px 0 0 0;display:flex;align-items:center;justify-content:center;gap:14px}
.dots span{width:12px;height:12px;border-radius:50%;background:#fff}
.dots span.on{background:#8b1e3a;box-shadow:0 0 0 2px #fff}
.panel{background:var(--panel);border-radius:4px}
.heading{font-family:"Fredoka",sans-serif;font-weight:600;font-size:18px;text-shadow:-1px -1px 0 #fff,1px -1px 0 #fff,-1px 1px 0 #fff,1px 1px 0 #fff,0 2px 3px rgba(0,0,0,.3)}
.pink{color:var(--pink)}.green{color:var(--green)}.orange{color:var(--orange)}
.copy{font-size:13.4px;line-height:19.6px;text-align:justify;hyphens:auto}
.frame{border:4px solid #fff;border-radius:16px;box-shadow:0 1px 4px rgba(0,0,0,.35)}
.events{left:646px;top:732px;width:330px}
.event{display:flex;gap:10px;font-size:13px;line-height:16px}
.event svg{flex:0 0 22px}
.event time{display:block;font-style:italic;font-size:11.5px;color:var(--date);margin-top:1px}
.divider{left:47px;top:915px;width:937px;height:3px;background:#ddd5d1}
.feature-title{font-family:"Fredoka",sans-serif;font-weight:600;font-size:19px;color:var(--brown-text);text-shadow:0 0 2px #fff,0 2px 3px rgba(0,0,0,.3)}
.feature-text{font-size:11.5px;line-height:16px;color:var(--brown-text)}
.subscribe-input{left:845px;top:984px;width:131px;height:22px;border-radius:11px;background:#d5ccc8;border:1px solid #fff;font-size:10.5px;color:#5a4a44;padding:4px 12px}
.subscribe-btn{left:935px;top:1012px;font-size:11px;font-weight:700;color:#b43a1c}
.footer{left:0;top:1058px;width:1030px;height:142px;background:var(--brown-dark);color:var(--footer-text)}
.fcol{position:absolute;top:22px;font-size:11.5px;line-height:21.6px}
.fcol h4{font-weight:400;font-size:13px;margin-bottom:2px}
.footer .copyright{left:598px;top:31px;font-size:11.5px}
.footer .connect{left:618px;top:81px;font-size:11.5px}
.social{position:absolute;top:73px;width:31px;height:31px;border-radius:50%;background:#fff}
</style>
</head>
<body>
<header>
  <div class="abs topbar"><span class="abs phone">Call us : 555 210 4782</span></div>
  <div class="abs logo"><span class="dot"></span>Frostwerkly.com</div>

  <svg class="abs" style="left:636px;top:55px" width="352" height="107" viewBox="0 0 352 107" aria-hidden="true">
    <path d="M2 107 V60 Q2 34 30 30 Q40 4 80 6 Q112 -2 138 22 Q176 18 186 60 V107 Z" fill="#a9c95b" stroke="#fff" stroke-width="3"/>
    <path d="M172 107 V70 Q172 44 200 42 Q210 18 250 22 Q278 14 300 36 Q346 38 350 80 V107 Z" fill="#d2427c" stroke="#fff" stroke-width="3"/>
  </svg>
  <div class="abs ph" role="img" aria-label="Illustration of a tiered birthday cake with candles" style="left:728px;top:64px;width:48px;height:42px;border-radius:10px;background:linear-gradient(180deg,#f3d9a0,#e8616a)"></div>
  <div class="abs ph" role="img" aria-label="Illustration of a red cherry" style="left:820px;top:72px;width:54px;height:46px;border-radius:12px;background:var(--cherry)"></div>
  <div class="abs cta" style="left:672px;top:112px">Submit an idea<br>for a cake</div>
  <div class="abs cta" style="left:823px;top:118px;font-size:15px">New designer ?<br><span style="margin-left:84px;color:#fbe0a0">Sign up</span></div>

  <div class="abs nav-frame"></div>
  <nav class="abs nav">
    <a class="active" style="width:100px">Home</a>
    <a style="width:108px">About Us</a>
    <a style="width:128px">Cake Designs</a>
    <a style="width:127px">Design Ideas</a>
    <a style="width:121px">Best Design</a>
    <a style="width:144px">Design Reviews</a>
    <a style="width:83px">Log in</a>
    <a style="width:131px">Contact Us</a>
  </nav>
  <div class="abs hero ph" role="img" aria-label="Soft photo of a pastry chef whisking cream in a bowl"></div>
  <div class="abs hero-cake ph" role="img" aria-label="Photo of a white wedding cake decorated with red and pink roses"></div>
  <div class="abs hero-title">Rose Petals</div>
  <div class="abs rating">Rating:
    <svg width="104" height="16" viewBox="0 0 104 16" aria-hidden="true">
      <g stroke="#b88a10" stroke-width=".6">
        <polygon points="8,1 10,6 15,6 11,9.5 12.5,15 8,11.8 3.5,15 5,9.5 1,6 6,6" fill="var(--star-gold)"/>
        <polygon transform="translate(22 0)" points="8,1 10,6 15,6 11,9.5 12.5,15 8,11.8 3.5,15 5,9.5 1,6 6,6" fill="var(--star-gold)"/>
        <polygon transform="translate(44 0)" points="8,1 10,6 15,6 11,9.5 12.5,15 8,11.8 3.5,15 5,9.5 1,6 6,6" fill="var(--star-gold)"/>
        <polygon transform="translate(66 0)" points="8,1 10,6 15,6 11,9.5 12.5,15 8,11.8 3.5,15 5,9.5 1,6 6,6" fill="var(--star-gold)"/>
        <polygon transform="translate(88 0)" points="8,1 10,6 15,6 11,9.5 12.5,15 8,11.8 3.5,15 5,9.5 1,6 6,6" fill="var(--star-grey)" stroke="#999"/>
      </g>
    </svg>
  </div>
  <a class="abs hero-more">View more</a>
  <div class="abs dots"><span class="on"></span><span></span><span></span><span></span><span></span></div>
</header>

<main>
  <section>
    <div class="abs panel" style="left:47px;top:499px;width:547px;height:164px"></div>
    <h2 class="abs heading pink" style="left:63px;top:484px">Welcome to our site</h2>
    <p class="abs copy" style="left:63px;top:520px;width:515px">consectetur adipisicing elit, sed do eiusmod tempor incididunt ut labore et dolore magna aliqua. Ut enim ad minim veniam, quis nostrud exercitation ullamco laboris nisi ut aliquip ex ea commodo consequat. Duis aute irure dolor in repre&shy;henderit in voluptate velit esse cillum dolore eu fugiat nulla pariatur. Excepteur sint occaecat cupidatat non proident, sunt in culpa qui officia deserunt mollit anim id est laborum.</p>
    <a class="abs heading pink" style="left:475px;top:648px;font-size:17px">View more</a>
    <div class="abs ph" role="img" aria-label="Illustration of a chocolate cake slice with cream and a cherry" style="left:564px;top:612px;width:56px;height:60px;border-radius:14px;background:linear-gradient(180deg,#f6eee8 0%,#8a4a1c 40%,#4e2a12 100%)"></div>
  </section>

  <section>
    <div class="abs panel" style="left:645px;top:499px;width:333px;height:166px"></div>
    <div class="abs ph" role="img" aria-label="Illustration of a golden trophy cup" style="left:626px;top:489px;width:44px;height:70px;border-radius:10px 10px 6px 6px;background:linear-gradient(180deg,#e9b94a,#8a5a1a)"></div>
    <h2 class="abs heading green" style="left:681px;top:484px">Latest Prize Winner</h2>
    <div class="abs frame ph" role="img" aria-label="Photo of the winning black and white tiered cake" style="left:687px;top:526px;width:98px;height:66px;background:linear-gradient(180deg,#6b4a3a,#e9e3de)"></div>
    <div class="abs frame ph" role="img" aria-label="Photo of the winning cake designer" style="left:825px;top:526px;width:98px;height:66px;background:linear-gradient(180deg,#5a8fd0,#b98a70)"></div>
    <p class="abs copy" style="left:690px;top:608px;width:268px">Duis aute irure dolor in reprehenderit in voluptate velit.</p>
  </section>

  <section>
    <div class="abs panel" style="left:47px;top:710px;width:547px;height:164px"></div>
    <h2 class="abs heading orange" style="left:63px;top:695px">Design Ideas</h2>
    <div class="abs frame ph" role="img" aria-label="Photo of a tiered cake with heart pattern and a sugar flower" style="left:64px;top:736px;width:181px;height:121px;border-width:5px;border-radius:22px;background:linear-gradient(180deg,#1c1c1c 0%,#d9b77a 30%,#f4f0ea 60%,#222 100%)"></div>
    <p class="abs copy" style="left:265px;top:733px;width:310px">Duis aute irure dolor in reprehenderit in voluptate velit esse cillum dolore eu fugiat nulla pariatur. Excepteur sint occaecat cupidatat non proident, sunt in culpa qui officia deserunt mollit anim id est laborum avoids a pain that produces no resultant pleasure.</p>
    <a class="abs heading green" style="left:403px;top:861px;font-size:16px">Submit Your's</a>
    <a class="abs heading orange" style="left:532px;top:860px;font-size:16px">View all</a>
  </section>

  <section>
    <h2 class="abs" style="left:645px;top:696px;font-size:17px;font-weight:700;color:var(--brown-text)">Latest Events</h2>
    <div class="abs events">
      <div class="event">
        <svg width="22" height="22" viewBox="0 0 22 22" aria-hidden="true"><circle cx="11" cy="11" r="9" fill="none" stroke="#7b6a62" stroke-width="1.6"/><polygon points="11,5 12.6,9 16.6,9 13.4,11.6 14.6,15.6 11,13.2 7.4,15.6 8.6,11.6 5.4,9 9.4,9" fill="#9b8a82"/></svg>
        <div>Excepteur sint occaecat cupidatat non proident, sunt in culpa qui officia.<time>Feb 4th Saturday</time></div>
      </div>
      <div class="event" style="margin-top:22px">
        <svg width="22" height="22" viewBox="0 0 22 22" aria-hidden="true"><circle cx="11" cy="11" r="9" fill="none" stroke="#7b6a62" stroke-width="1.6"/><polygon points="11,5 12.6,9 16.6,9 13.4,11.6 14.6,15.6 11,13.2 7.4,15.6 8.6,11.6 5.4,9 9.4,9" fill="#9b8a82"/></svg>
        <div>Occaecat cupidatat non culpa qui officia.<time>Feb 11th Saturday</time></div>
      </div>
      <div class="event" style="margin-top:24px">
        <svg width="22" height="22" viewBox="0 0 22 22" aria-hidden="true"><circle cx="11" cy="11" r="9" fill="none" stroke="#7b6a62" stroke-width="1.6"/><polygon points="11,5 12.6,9 16.6,9 13.4,11.6 14.6,15.6 11,13.2 7.4,15.6 8.6,11.6 5.4,9 9.4,9" fill="#9b8a82"/></svg>
        <div>Excepteur sint occaecat cupidatat non proident, sunt in culpa qui officia.<time>Feb 18th Saturday</time></div>
      </div>
    </div>
  </section>

  <div class="abs divider"></div>

  <section>
    <div class="abs ph" role="img" aria-label="Illustration of two friends" style="left:58px;top:946px;width:72px;height:76px;border-radius:20px;background:linear-gradient(135deg,#9bc47a,#4a86c6)"></div>
    <h3 class="abs feature-title" style="left:136px;top:952px">Tell a Friend</h3>
    <p class="abs feature-text" style="left:141px;top:986px">Invite Friends now</p>

    <div class="abs ph" role="img" aria-label="Illustration of a chef in a tall hat" style="left:311px;top:946px;width:50px;height:76px;border-radius:16px;background:linear-gradient(180deg,#f2f2f2,#9a9a9a)"></div>
    <h3 class="abs feature-title" style="left:372px;top:952px">Meet Chefs</h3>
    <p class="abs feature-text" style="left:373px;top:986px">Speak with Cake<br>Designers</p>

    <div class="abs ph" role="img" aria-label="Illustration of a birthday cake with candles and a magnifying glass" style="left:525px;top:948px;width:60px;height:68px;border-radius:18px;background:linear-gradient(180deg,#f7c74a,#6c9fd8)"></div>
    <h3 class="abs feature-title" style="left:591px;top:952px">Search a Flavour</h3>
    <p class="abs feature-text" style="left:604px;top:986px">Search a flavour cake<br>Design</p>

    <div class="abs ph" role="img" aria-label="Illustration of a red heart with a laptop" style="left:773px;top:948px;width:64px;height:66px;border-radius:18px;background:linear-gradient(135deg,#e52a2a,#9a9a9a)"></div>
    <h3 class="abs feature-title" style="left:845px;top:952px">Subscribe</h3>
    <div class="abs subscribe-input">Enter mail ID</div>
    <span class="abs subscribe-btn">SUBMIT</span>
  </section>
</main>

<footer class="abs footer">
  <div class="fcol" style="left:60px"><h4>Heading 1</h4>Footer Link 1<br>Footer Link 2<br>Footer Link 3<br>Footer Link 4</div>
  <div class="fcol" style="left:188px"><h4>Heading 2</h4>Footer Link 1<br>Footer Link 2<br>Footer Link 3<br>Footer Link 4</div>
  <div class="fcol" style="left:317px"><h4>Heading 3</h4>Footer Link 1<br>Footer Link 2<br>Footer Link 3<br>Footer Link 4</div>
  <div class="fcol" style="left:445px"><h4>Heading 4</h4>Footer Link 1<br>Footer Link 2<br>Footer Link 3<br>Footer Link 4</div>
  <p class="abs copyright">Copyright © 2012 wwwfrostwerkly.com &nbsp;All rights reserved</p>
  <p class="abs connect">Connect with us :</p>
  <span class="social" style="left:722px"></span>
  <span class="social" style="left:760px"></span>
  <span class="social" style="left:797px"></span>
  <span class="social" style="left:835px"></span>
  <span class="social" style="left:872px"></span>
</footer>
</body>
</html>
```